hi all

Im after a new age looking business card with my company logo on it

must include these details, I would like the PH and Email to be symbols

If the colours used for card could be kept within the colours used in logo that I have supplied that would be great, if another colour is to be used dark grey would be ok. no light bulbs etc thanks

Details below to be incorporated on card

Damian Holloway

Lic E871302

PH 0219647381

E info@brightvaleelectrical.example.nz

Domestic Commercial Industrial Electricians

```html
<!DOCTYPE html>
<html lang="en">
<head>
<meta charset="utf-8">
<title>Brightvale Electrical – Business Card</title>
<link rel="stylesheet" href="https://fonts.googleapis.com/css2?family=Montserrat:wght@700&family=Oswald:wght@300;400&display=swap">
<style>
  :root {
    --page-bg: #ffffff;
    --card-edge: #1d1d1d;
    --brand-blue: #1a75bb;
    --band-blue: #00adef;
    --band-blue-deep: #0a86bf;
    --band-dark: #2a2f38;
    --text-light: #ffffff;
  }
  html, body {
    margin: 0;
    padding: 0;
    width: 1200px;
    height: 1000px;
    overflow: hidden;
    background: var(--page-bg);
  }
  .canvas {
    position: relative;
    width: 1200px;
    height: 1000px;
  }
  .card-art {
    position: absolute;
    inset: 0;
  }
  .brand-name {
    position: absolute;
    left: 160px;
    top: 377px;
    width: 396px;
    margin: 0;
    font-family: "Montserrat", sans-serif;
    font-weight: 700;
    color: var(--brand-blue);
    text-align: right;
    line-height: 1;
  }
  .brand-name__main {
    display: block;
    font-size: 56px;
    letter-spacing: 0;
  }
  .brand-name__sub {
    display: block;
    margin-top: 8px;
    margin-right: -5px;
    font-size: 22px;
    letter-spacing: 5px;
  }
  .tagline {
    position: absolute;
    left: 653px;
    top: 721px;
    margin: 0;
    font-family: "Oswald", sans-serif;
    font-weight: 400;
    font-size: 21px;
    letter-spacing: 1.8px;
    word-spacing: 3px;
    color: var(--text-light);
    white-space: nowrap;
  }
</style>
</head>
<body>
<main class="canvas">
  <svg class="card-art" width="1200" height="1000" viewBox="0 0 1200 1000">
    <defs>
      <linearGradient id="bandPatternTone" x1="0" y1="0" x2="1" y2="1">
        <stop offset="0" stop-color="var(--band-blue-deep)"/>
        <stop offset="0.45" stop-color="var(--band-blue)"/>
        <stop offset="1" stop-color="var(--band-blue-deep)"/>
      </linearGradient>
    </defs>

    <rect class="card-surface" x="37.5" y="162.5" width="1126" height="676" fill="#ffffff" stroke="var(--card-edge)" stroke-width="1"/>

    <path class="band-blue" role="img" aria-label="Geometric pattern of overlapping blue triangles joined by thin network lines and dots"
      fill="url(#bandPatternTone)"
      d="M38,508 H600 C618,508 626,502 638,490 L654,475 C664,467 672,465 690,465 H1163 V690 H38 Z"/>

    <path class="band-dark" fill="var(--band-dark)"
      d="M38,685 H600 C618,685 626,679 638,667 L654,652 C664,644 672,640 690,640 H1163 V838 H38 Z"/>
  </svg>

  <h1 class="brand-name">
    <span class="brand-name__main">BRIGHTVALE</span>
    <span class="brand-name__sub">ELECTRICAL</span>
  </h1>

  <p class="tagline">Domestic Commercial Industrial Electricians</p>
</main>
</body>
</html>
```